Professional business cards for real estate development company

I need business cards for my new real estate development company. The company, "KORVA" is a real estate development, investment, and advisory firm with a focus on multifamily, office, and mixed-use projects across primary and secondary markets in the Southeast United States.

Style preference is modern

Industry/Entity Type

Real Estate Development

Contact Information for Business Card

The business cards need to include:
Name
Title
Mailing Address
Phone Number
Web Address

Logo is attached. I would like white to be the primary color with incorporation of the company colors: #232D3A and #B5A451

Font styles to use
Other font styles liked:
• Montserrat, Avenir

Requirements
Must have
• Company Logo. No need to include the company name since the name is in the logo.
Should not have
• No line type designs

```html
<!DOCTYPE html>
<html lang="en">
<head>
<meta charset="UTF-8">
<title>KORVA Development – Business Cards</title>
<link rel="stylesheet" href="https://fonts.googleapis.com/css2?family=Montserrat:wght@400;600;700&display=swap">
<style>
  :root {
    --backdrop: #dfe1e4;
    --card: #ffffff;
    --navy: #232d3a;
    --navy-soft: #4a5564;
    --gold: #b5a451;
  }
  * { margin: 0; padding: 0; box-sizing: border-box; }
  html, body { width: 1200px; height: 900px; overflow: hidden; }
  body {
    background: var(--backdrop);
    font-family: "Montserrat", sans-serif;
    display: flex;
    flex-direction: column;
    align-items: center;
    justify-content: center;
    gap: 40px;
  }
  .card {
    width: 700px;
    height: 400px;
    background: var(--card);
    border-radius: 6px;
    box-shadow: 0 12px 30px rgba(35,45,58,.18);
    position: relative;
    overflow: hidden;
  }

  /* shared wordmark */
  .wordmark {
    display: flex;
    align-items: center;
    gap: 14px;
    color: var(--navy);
    font-weight: 700;
    letter-spacing: .06em;
    line-height: 1.05;
  }
  .wordmark-square {
    width: 18px; height: 18px;
    background: var(--gold);
    flex: none;
  }

  /* front */
  .card-front { display: flex; align-items: center; }
  .front-brand {
    width: 370px;
    display: flex;
    justify-content: flex-end;
    padding-right: 44px;
  }
  .front-brand .wordmark { font-size: 30px; }
  .front-brand .wordmark span { display: block; }
  .front-details { padding-left: 16px; color: var(--navy); }
  .person-name {
    font-size: 24px; font-weight: 700;
    letter-spacing: .02em;
    color: var(--navy);
  }
  .person-title {
    font-size: 17px; font-weight: 600; color: var(--gold);
    margin-top: 4px; margin-bottom: 20px;
  }
  .contact-list { list-style: none; }
  .contact-item {
    display: flex; align-items: flex-start; gap: 12px;
    font-size: 15px; line-height: 1.35; margin-bottom: 9px;
    color: var(--navy-soft);
  }
  .contact-icon { width: 18px; height: 18px; flex: none; margin-top: 1px; }

  /* back */
  .card-back {
    display: flex; flex-direction: column;
    align-items: center; justify-content: center;
  }
  .card-back .wordmark { font-size: 40px; margin-top: -30px; }
  .back-web {
    position: absolute; left: 0; right: 0; bottom: 50px;
    text-align: center;
    font-size: 16px; font-weight: 600; color: var(--gold); letter-spacing: .02em;
  }
</style>
</head>
<body>

  <section class="card card-front" aria-label="Business card front">
    <div class="front-brand">
      <div class="wordmark">
        <div class="wordmark-square"></div>
        <div>
          <span>KORVA</span>
          <span>DEVELOPMENT</span>
        </div>
      </div>
    </div>
    <div class="front-details">
      <p class="person-name">DANA WHITLOCK</p>
      <p class="person-title">President</p>
      <ul class="contact-list">
        <li class="contact-item">
          <svg class="contact-icon" viewBox="0 0 24 24" aria-hidden="true">
            <path d="M12 2a7 7 0 0 0-7 7c0 5 7 13 7 13s7-8 7-13a7 7 0 0 0-7-7zm0 9.5A2.5 2.5 0 1 1 12 6.5a2.5 2.5 0 0 1 0 5z" fill="#b5a451"/>
          </svg>
          <span>1200 Example Ave, Suite 400<br>Atlanta, GA 30301</span>
        </li>
        <li class="contact-item">
          <svg class="contact-icon" viewBox="0 0 24 24" aria-hidden="true">
            <path d="M6.6 10.8a15.1 15.1 0 0 0 6.6 6.6l2.2-2.2a1 1 0 0 1 1-.25 11.4 11.4 0 0 0 3.6.57 1 1 0 0 1 1 1V20a1 1 0 0 1-1 1A17 17 0 0 1 3 4a1 1 0 0 1 1-1h3.5a1 1 0 0 1 1 1c0 1.25.2 2.45.57 3.57a1 1 0 0 1-.25 1z" fill="#b5a451"/>
          </svg>
          555.014.2230
        </li>
        <li class="contact-item">
          <svg class="contact-icon" viewBox="0 0 24 24" aria-hidden="true">
            <rect x="2" y="5" width="20" height="14" rx="1.5" fill="#b5a451"/>
            <path d="M3 6l9 7 9-7" stroke="#ffffff" stroke-width="1.6" fill="none"/>
          </svg>
          info@korvamail.com
        </li>
        <li class="contact-item">
          <svg class="contact-icon" viewBox="0 0 24 24" aria-hidden="true">
            <circle cx="12" cy="12" r="10" fill="#b5a451"/>
            <path d="M2 12h20M12 2c3 3 3 17 0 20M12 2c-3 3-3 17 0 20" stroke="#ffffff" stroke-width="1.3" fill="none"/>
          </svg>
          www.korvasite.com
        </li>
      </ul>
    </div>
  </section>

  <section class="card card-back" aria-label="Business card back">
    <div class="wordmark">
      <div class="wordmark-square"></div>
      <span>KORVA DEVELOPMENT</span>
    </div>
    <p class="back-web">www.korvadevelopment.com</p>
  </section>

</body>
</html>
```